Website for my photography business

I need a website for my photography business, Jonah Pelling Photography. I need a website that has a landing page with a cover photo of each kind of photography I do. For example, Nature, Weddings, Portraits and Architecture. I want it so that when someone comes onto my website they have to choose which kind of photography page they want to visit. So if they click on the wedding photo it will open to a page with my wedding portfolio images and a contact me button. If they choose nature photography I want them to be redirected to an e-commerce section where they can purchase prints. Architecture and Portraits should open up to their respective portfolios with about me and contact info. I like this kind of format because I want people who come to my website for a specific type of photography to be able to be directed there easily without having to look at a mix of other kinds of photography. I will provide a few files to use as placeholders. I have already purchased the jonahpellingphotography.example domain name. A Wix website would be great because I am most familiar with it but I am open to anything.

Industry/Entity Type

Photographer

Number of Pages Required

5+ page

Requirements
Must have
• Landing Page and e-commerce

```html
<!DOCTYPE html>
<html lang="en">
<head>
<meta charset="utf-8">
<title>Jonah Pelling Photography</title>
<link rel="stylesheet" href="https://fonts.googleapis.com/css2?family=Amatic+SC:wght@400;700&family=Jost:wght@300;400;500;600&display=swap">
<style>
  :root {
    --white: #ffffff;
    --ink: #1e1e1e;
    --muted: #8c8c8c;
    --accent: #e8575a;
    --button: #555555;
    --rule: #d9d9d9;
    --panel: #f1f1f1;
    --peach: #f9dfc6;
    --card-border: #e6e6e6;
  }
  * { margin: 0; padding: 0; box-sizing: border-box; }
  html, body { width: 1200px; height: 3600px; overflow: hidden; background: var(--white); }
  body { position: relative; font-family: "Jost", sans-serif; color: var(--ink); }
  a { text-decoration: none; color: inherit; }
  .abs { position: absolute; }

  /* Header */
  .site-header { left: 0; top: 0; width: 1200px; height: 67px; background: var(--white); }
  .brand { left: 158px; top: 14px; font-family: "Amatic SC", sans-serif; font-weight: 700; font-size: 29px; letter-spacing: 1px; text-transform: uppercase; color: var(--ink); }
  .nav-link { top: 22px; font-size: 15px; font-weight: 400; color: var(--ink); }
  .nav-link.is-active { color: var(--accent); }
  .cart { left: 966px; top: 22px; display: flex; align-items: center; gap: 6px; font-size: 15px; color: var(--muted); }
  .social-dot { left: 1017px; top: 20px; width: 27px; height: 27px; border-radius: 50%; background: var(--ink); }

  /* Hero */
  .hero { left: 0; top: 67px; width: 1200px; height: 571px;
    background: linear-gradient(180deg, #f4e9df 0%, #e7d2bd 28%, #b59a7d 50%, #6f7d62 72%, #4f6a6a 100%); }
  .hero-title { left: 0; top: 165px; width: 1200px; text-align: center; font-family: "Amatic SC", sans-serif; font-weight: 400; font-size: 96px; letter-spacing: 8px; line-height: 1; text-transform: uppercase; color: var(--ink); }
  .hero-text { left: 268px; top: 272px; width: 664px; text-align: center; font-size: 16px; line-height: 21px; letter-spacing: 0.3px; color: var(--ink); }

  /* Section headings */
  .section-title { font-family: "Amatic SC", sans-serif; font-weight: 400; font-size: 58px; letter-spacing: 2px; line-height: 1; color: var(--ink); }
  .section-title.is-caps { text-transform: uppercase; font-size: 52px; }

  /* Gallery */
  .photo { display: block; overflow: hidden; }
  .photo-meta { position: absolute; bottom: 14px; left: 14px; display: flex; align-items: center; gap: 4px; font-size: 15px; color: var(--white); }
  .photo-share { position: absolute; bottom: 14px; right: 14px; }
  .photo-category { position: absolute; bottom: 30px; left: 0; width: 100%; text-align: center; font-size: 13px; font-weight: 500; letter-spacing: 3px; text-transform: uppercase; color: var(--white); }
  .btn { display: flex; align-items: center; justify-content: center; background: var(--button); color: var(--white); font-size: 13px; font-weight: 600; letter-spacing: 1.8px; text-transform: uppercase; }

  /* Posts */
  .post-card { left: 158px; width: 884px; height: 323px; border: 1px solid var(--card-border); background: var(--white); }
  .post-image { position: absolute; left: 0; top: 0; width: 450px; height: 321px; }
  .post-body { position: absolute; left: 517px; top: 0; width: 341px; height: 321px; }
  .post-date { position: absolute; top: 46px; font-size: 12px; color: var(--muted); }
  .post-title { position: absolute; top: 70px; width: 330px; font-size: 19.5px; line-height: 26px; color: var(--ink); }
  .post-excerpt { position: absolute; top: 134px; width: 332px; font-size: 15.5px; line-height: 20px; letter-spacing: 0.5px; color: var(--muted); }
  .post-rule { position: absolute; top: 240px; left: 0; width: 341px; height: 1px; background: var(--rule); }
  .post-views { position: absolute; top: 262px; font-size: 13px; color: var(--muted); }
  .post-likes { position: absolute; top: 261px; right: 8px; display: flex; align-items: center; gap: 4px; font-size: 14px; color: var(--muted); }

  /* About */
  .about-panel { left: 0; top: 3009px; width: 578px; height: 498px; background: var(--panel); }
  .about-title { right: 696px; top: 3140px; text-align: right; }
  .about-text { left: 172px; top: 3208px; width: 332px; text-align: right; font-size: 16px; line-height: 20.5px; letter-spacing: 0.3px; color: var(--muted); }
  .about-image { left: 578px; top: 3009px; width: 622px; height: 498px;
    background: linear-gradient(90deg, #3b3633 0%, #6b5a4d 40%, #5a5856 75%, #4a4c4e 100%); }
  .about-band { left: 786px; top: 3009px; width: 207px; height: 498px; background: rgba(232, 87, 90, 0.82); }

  /* Contact */
  .contact-band { left: 0; top: 3507px; width: 1200px; height: 93px; background: var(--peach); }
  .contact-title { left: 0; top: 3542px; width: 1200px; text-align: center; }
</style>
</head>
<body>

<header class="abs site-header">
  <div class="abs brand">JonahPellingPhotography</div>
  <a class="abs nav-link is-active" style="left:521px">Home</a>
  <a class="abs nav-link" style="left:601px">About</a>
  <a class="abs nav-link" style="left:681px">Photography</a>
  <a class="abs nav-link" style="left:803px">Contact</a>
  <a class="abs nav-link" style="left:899px">Prints</a>
  <div class="abs cart">
    <svg width="16" height="18" viewBox="0 0 16 18" fill="none" stroke="#555" stroke-width="1.3"><path d="M2 5h12l-1 12H3z"/><path d="M5 7V4a3 3 0 0 1 6 0v3"/></svg>
    <span>0</span>
  </div>
  <div class="abs social-dot" aria-label="Social profile"></div>
</header>

<section class="abs hero" role="img" aria-label="Aerial landscape of a bay with green hills and coastline at sunrise"></section>
<h1 class="abs hero-title">That Open River</h1>
<p class="abs hero-text">Many desktop publishing packages and web page editors now use Lorem Ipsum as their default model text, and a search for 'lorem ipsum' will uncover manytheir infancy.</p>

<h2 class="abs section-title is-caps" style="left:158px;top:690px">Photography</h2>

<a class="abs photo" href="#weddings" style="left:158px;top:794px;width:450px;height:363px;background:linear-gradient(180deg,#bfc3c4 0%,#6d6a66 45%,#4a4744 75%,#cfcac4 100%)" role="img" aria-label="Weddings: couple embracing beneath a colonnade bridge">
  <div class="photo-category">Weddings</div>
  <div class="photo-meta"><svg width="16" height="14" viewBox="0 0 16 14" fill="none" stroke="#fff" stroke-width="1.3"><path d="M8 13S1 8.5 1 4.5A3.3 3.3 0 0 1 8 3a3.3 3.3 0 0 1 7 1.5C15 8.5 8 13 8 13z"/></svg>12</div>
  <svg class="photo-share" width="16" height="14" viewBox="0 0 16 14" fill="none" stroke="#fff" stroke-width="1.3"><path d="M10 1l5 4.5L10 10V7C5 7 2 9 1 13c0-5 3-9 9-9.5z"/></svg>
</a>
<a class="abs btn" href="#contact" style="left:296px;top:1048px;width:173px;height:50px">Contact Us</a>

<a class="abs photo" href="#portraits" style="left:676px;top:714px;width:366px;height:514px;background:linear-gradient(160deg,#a77b4c 0%,#b88a5a 45%,#c9a27a 70%,#e8e2da 100%)" role="img" aria-label="Portraits: woman in a cream knit sweater on a warm brown backdrop">
  <div class="photo-category">Portraits</div>
  <div class="photo-meta"><svg width="16" height="14" viewBox="0 0 16 14" fill="none" stroke="#fff" stroke-width="1.3"><path d="M8 13S1 8.5 1 4.5A3.3 3.3 0 0 1 8 3a3.3 3.3 0 0 1 7 1.5C15 8.5 8 13 8 13z"/></svg>12</div>
</a>

<a class="abs photo" href="#architecture" style="left:158px;top:1182px;width:367px;height:514px;background:linear-gradient(135deg,#9aa0a6 0%,#5b6068 40%,#2f3338 60%,#8d939a 100%)" role="img" aria-label="Architecture: looking up through a glass and steel grid atrium">
  <div class="photo-category">Architecture</div>
  <div class="photo-meta"><svg width="16" height="14" viewBox="0 0 16 14" fill="none" stroke="#fff" stroke-width="1.3"><path d="M8 13S1 8.5 1 4.5A3.3 3.3 0 0 1 8 3a3.3 3.3 0 0 1 7 1.5C15 8.5 8 13 8 13z"/></svg>12</div>
  <svg class="photo-share" width="16" height="14" viewBox="0 0 16 14" fill="none" stroke="#fff" stroke-width="1.3"><path d="M10 1l5 4.5L10 10V7C5 7 2 9 1 13c0-5 3-9 9-9.5z"/></svg>
</a>

<a class="abs photo" href="#prints" style="left:594px;top:1267px;width:448px;height:362px;background:linear-gradient(180deg,#3f6c93 0%,#8fb2cb 45%,#c48a3a 62%,#5e5c58 80%,#77787a 100%)" role="img" aria-label="Nature: straight country road lined with autumn trees under a blue sky">
  <div class="photo-category">Nature</div>
  <div class="photo-meta"><svg width="16" height="14" viewBox="0 0 16 14" fill="none" stroke="#fff" stroke-width="1.3"><path d="M8 13S1 8.5 1 4.5A3.3 3.3 0 0 1 8 3a3.3 3.3 0 0 1 7 1.5C15 8.5 8 13 8 13z"/></svg>12</div>
  <svg class="photo-share" width="16" height="14" viewBox="0 0 16 14" fill="none" stroke="#fff" stroke-width="1.3"><path d="M10 1l5 4.5L10 10V7C5 7 2 9 1 13c0-5 3-9 9-9.5z"/></svg>
</a>

<h2 class="abs section-title" style="left:158px;top:1780px">Latest Posts</h2>

<article class="abs post-card" style="top:1861px">
  <div class="post-image" style="background:linear-gradient(180deg,#b9b4ae 0%,#7c6a4c 25%,#9a7c44 55%,#4c4a4a 85%,#c9a63b 100%)" role="img" aria-label="Winding road through golden grassland hills"></div>
  <div class="post-body">
    <div class="post-date">April 29,2020 .&nbsp; 6 min</div>
    <div class="post-title">It is a long established fact that a readerwill be distracted content</div>
    <div class="post-excerpt">Many desktop publishing packages and web page editors now use Lorem Ipsum as their default model text, and a search for 'lorem ipsum' will uncover manytheir infancy.</div>
    <div class="post-rule"></div>
    <div class="post-views">55 views</div>
    <div class="post-likes"><svg width="15" height="13" viewBox="0 0 16 14" fill="none" stroke="#e8575a" stroke-width="1.5"><path d="M8 13S1 8.5 1 4.5A3.3 3.3 0 0 1 8 3a3.3 3.3 0 0 1 7 1.5C15 8.5 8 13 8 13z"/></svg>12</div>
  </div>
</article>

<article class="abs post-card" style="top:2199px">
  <div class="post-image" style="background:linear-gradient(180deg,#c6cdd6 0%,#a8a6a8 35%,#b06a3a 55%,#4a2f2a 80%,#2d2426 100%)" role="img" aria-label="Curving copper-clad modern building reflected in water"></div>
  <div class="post-body">
    <div class="post-date">April 29,2020 .&nbsp; 6 min</div>
    <div class="post-title">It is a long established fact that a readerwill be distracted content</div>
    <div class="post-excerpt">Many desktop publishing packages and web page editors now use Lorem Ipsum as their default model text, and a search for 'lorem ipsum' will uncover manytheir infancy.</div>
    <div class="post-rule"></div>
    <div class="post-views">55 views</div>
    <div class="post-likes"><svg width="15" height="13" viewBox="0 0 16 14" fill="none" stroke="#e8575a" stroke-width="1.5"><path d="M8 13S1 8.5 1 4.5A3.3 3.3 0 0 1 8 3a3.3 3.3 0 0 1 7 1.5C15 8.5 8 13 8 13z"/></svg>12</div>
  </div>
</article>

<article class="abs post-card" style="top:2537px">
  <div class="post-image" style="background:linear-gradient(180deg,#8a6fc4 0%,#c9a0d8 35%,#e8b8c8 48%,#3b3a78 62%,#2a2450 100%)" role="img" aria-label="Footbridge leading toward a domed cathedral at purple dusk"></div>
  <div class="post-body">
    <div class="post-date">April 29,2020 .&nbsp; 6 min</div>
    <div class="post-title">It is a long established fact that a readerwill be distracted content</div>
    <div class="post-excerpt">Many desktop publishing packages and web page editors now use Lorem Ipsum as their default model text, and a search for 'lorem ipsum' will uncover manytheir infancy.</div>
    <div class="post-rule"></div>
    <div class="post-views">55 views</div>
    <div class="post-likes"><svg width="15" height="13" viewBox="0 0 16 14" fill="none" stroke="#e8575a" stroke-width="1.5"><path d="M8 13S1 8.5 1 4.5A3.3 3.3 0 0 1 8 3a3.3 3.3 0 0 1 7 1.5C15 8.5 8 13 8 13z"/></svg>12</div>
  </div>
</article>

<div class="abs btn" style="left:513px;top:2885px;width:173px;height:52px">View All Posts</div>

<section class="abs about-panel"></section>
<h2 class="abs section-title about-title">About Me</h2>
<p class="abs about-text">Many desktop publishing packages and web page editors now use Lorem Ipsum as their default model text, and a search for 'lorem ipsum' will uncover many web sites still in their infancy. Various versions have evolved over the years, sometimes by accident, sometimes on purpose (injected humour and the like).</p>
<div class="abs about-image" role="img" aria-label="Photographer kneeling outdoors with a camera and backpack"></div>
<div class="abs about-band"></div>

<section class="abs contact-band" id="contact"></section>
<h2 class="abs section-title contact-title">Get In Touch</h2>

</body>
</html>
```